Product label for specialty fertilizer for cannabis

Create a label with our brand name and product information. The name of the new product is “Dravel” and the name is also the logo. The color palate is white/platinium/silver/shimmery. The product makes the flowers dense and hard so we want the logo to look strong and masculine. The liquid inside the bottle is white Which is what dravel means in Spanish
Also need a font for all the product information. See pics for example and
Target Market(s)
Cannabis growers
Industry/Entity Type
Cannabis
Colors
Designer to choose colors to be used in the design.
Requirements
Must have
- Strong visual presence for retail environment. Clean but bold look.
Nice to have
- Would be nice to have similar to a Fizzo Brava font
Should not have
- Do not put any cannabis or marijuana images anywhere on the label

```html
<!DOCTYPE html>
<html lang="en">
<head>
<meta charset="utf-8">
<title>Dravel Fertilizer Label</title>
<link rel="stylesheet" href="https://fonts.googleapis.com/css2?family=Bebas+Neue&family=Oswald:wght@400;500;600;700&family=Arimo:wght@400&display=swap">
<style>
  :root {
    --ink: #1c1c1c;
    --ink-deep: #0c0c0c;
    --olive: #4d5a2f;
    --olive-text: #56622f;
    --silver: #e6e6e8;
    --muted: #a9a9ab;
    --line: #8d8d92;
    --soil-1: #6b5132;
    --soil-2: #3a2b1b;
  }
  * { margin: 0; padding: 0; box-sizing: border-box; }
  html, body { width: 1200px; height: 600px; overflow: hidden; background: var(--ink); }
  .label { position: relative; width: 1200px; height: 600px; background: var(--ink); overflow: hidden; color: var(--silver); }
  .abs { position: absolute; }

  /* Directions panel */
  .directions-frame { left: 25px; top: 19px; width: 86px; height: 560px; background: var(--olive); }
  .directions-inner { left: 36px; top: 36px; width: 63px; height: 527px; border: 3px solid var(--ink-deep); }
  .directions-text {
    left: 44px; top: 44px; width: 50px; height: 510px;
    writing-mode: vertical-rl; transform: rotate(180deg);
    font-family: "Oswald", sans-serif; color: var(--silver);
  }
  .directions-title { font-weight: 600; font-size: 15px; line-height: 22px; text-align: center; letter-spacing: 0.2px; }
  .directions-body { font-family: "Bebas Neue", sans-serif; font-size: 9.5px; line-height: 15px; color: #cfcfcf; letter-spacing: 0.1px; }

  .maker {
    left: 200px; top: 330px; width: 46px; height: 254px;
    writing-mode: vertical-rl; transform: rotate(180deg);
    color: var(--silver); font-family: "Arimo", sans-serif;
  }
  .maker-title { font-family: "Oswald", sans-serif; font-weight: 700; font-size: 15px; line-height: 17px; }
  .maker-line { font-size: 8px; line-height: 11px; }

  /* Side strips */
  .strip { top: 0; width: 70px; height: 600px; background: var(--olive); }
  .strip-left { left: 249px; }
  .strip-right { left: 876px; }

  /* Hero */
  .hero { left: 319px; top: 0; width: 557px; height: 600px; }
  .soil {
    left: 319px; top: 0; width: 557px; height: 470px;
    background: linear-gradient(180deg, var(--soil-1) 0%, var(--soil-2) 55%, var(--ink) 100%);
  }
  .ring { left: 319px; top: 0; }
  .brand-name {
    left: 319px; top: 175px; width: 557px; text-align: center;
    font-family: "Bebas Neue", sans-serif; font-size: 150px; line-height: 150px;
    color: var(--silver); letter-spacing: 4px;
  }

  .claim-box { left: 388px; top: 476px; }
  .claim {
    left: 388px; top: 486px; width: 424px; text-align: center;
    font-family: "Bebas Neue", sans-serif; font-size: 35px; line-height: 36px; color: var(--olive-text);
  }
  .net-weight {
    left: 388px; top: 533px; width: 424px; text-align: center;
    font-family: "Oswald", sans-serif; font-weight: 500; font-size: 17px; line-height: 24px;
    letter-spacing: 7.5px; color: var(--silver);
  }

  /* Right panel */
  .banner { left: 996px; top: 0; }
  .banner-name {
    left: 1020px; top: 68px; width: 106px; text-align: center;
    font-family: "Bebas Neue", sans-serif; font-size: 34px; line-height: 34px; color: var(--silver);
  }
  .info-box { left: 964px; top: 228px; }
  .info-text {
    left: 975px; top: 236px; width: 200px;
    font-family: "Arimo", sans-serif; font-size: 9.5px; line-height: 12px;
    text-align: justify; color: var(--muted);
  }
  .info-text p + p { margin-top: 12px; }

  .hazard { left: 952px; top: 505px; }
  .hazard-pill {
    left: 1016px; top: 514px; width: 171px; height: 19px; border-radius: 10px;
    background: var(--ink-deep); border: 1px solid #3a3a3a;
    font-family: "Bebas Neue", sans-serif; font-size: 15px; line-height: 18px;
    color: var(--silver); padding-left: 10px;
  }
  .plant-only {
    left: 1027px; top: 532px;
    font-family: "Oswald", sans-serif; font-size: 12px; line-height: 16px;
    letter-spacing: 2.6px; color: var(--silver);
  }
  .warning-note {
    left: 1027px; top: 547px; width: 165px;
    font-family: "Arimo", sans-serif; font-size: 6px; line-height: 8px; color: #5c5c5c;
  }
</style>
</head>
<body>
<main class="label">

  <!-- Left panel: directions -->
  <div class="abs directions-frame"></div>
  <div class="abs directions-inner"></div>
  <div class="abs directions-text">
    <div class="directions-title">DIRECTIONS: SHAKE WELL BEFORE USE</div>
    <div class="directions-body">Spread the fertilizer over the garden area and disk or rake it into the top 4 inches of soil before planting each crop. Or you can apply the fertilizer to</div>
    <div class="directions-body">the soil just before spading or plowing in the spring or fall. Use starter fertilizer when transplanting to give your plants a faster start.</div>
  </div>

  <div class="abs maker">
    <div class="maker-title">MANUFACTURED BY:</div>
    <div class="maker-line"><b>DRAVEL FARMS</b>, HOLLOW CREEK RD. CA, 90610</div>
    <div class="maker-line">www. dravelfertilizers.com</div>
  </div>

  <!-- Side strips -->
  <div class="abs strip strip-left" role="img" aria-label="Olive band with a repeating black chevron pattern"></div>
  <div class="abs strip strip-right" role="img" aria-label="Olive band with a repeating black chevron pattern"></div>

  <!-- Hero -->
  <div class="abs soil" role="img" aria-label="Close-up photo of dark rich soil fading into black"></div>
  <svg class="abs ring" width="557" height="600" viewBox="0 0 557 600" aria-hidden="true">
    <circle cx="279" cy="232" r="196" fill="none" stroke="#6f6f76" stroke-width="3"/>
    <circle cx="279" cy="232" r="180" fill="none" stroke="#e4e4e6" stroke-width="2"/>
  </svg>
  <div class="abs brand-name">Dravel</div>

  <svg class="abs claim-box" width="424" height="90" viewBox="0 0 424 90" aria-hidden="true">
    <path d="M1 10 V2 H423 V10" fill="none" stroke="var(--line)" stroke-width="1.5"/>
    <path d="M1 80 V88 H423 V80" fill="none" stroke="var(--line)" stroke-width="1.5"/>
    <line x1="6" y1="51" x2="418" y2="51" stroke="var(--line)" stroke-width="1.2"/>
    <path d="M10 47 L4 51 L10 55 M414 47 L420 51 L414 55" fill="none" stroke="var(--line)" stroke-width="1.2"/>
  </svg>
  <div class="abs claim">ALL NATURAL, GROWERS APPROVED!</div>
  <div class="abs net-weight">NET WT. 24 OZ. (1.5LB) 680 G</div>

  <!-- Right panel -->
  <svg class="abs banner" width="157" height="226" viewBox="0 0 157 226" aria-hidden="true">
    <path d="M0 0 H157 V155 L78 226 L0 155 Z" fill="var(--ink-deep)"/>
    <path d="M4 0 H153 V100 L78 168 L4 100 Z" fill="var(--olive)"/>
  </svg>
  <div class="abs banner-name">Dravel</div>

  <svg class="abs info-box" width="221" height="262" viewBox="0 0 221 262" aria-hidden="true">
    <path d="M1 8 V1 H220 V8" fill="none" stroke="#6a6a6e" stroke-width="1.5"/>
    <path d="M1 253 V260 H220 V253" fill="none" stroke="#6a6a6e" stroke-width="1.5"/>
  </svg>
  <div class="abs info-text">
    <p>Lorem Ipsum is simply dummy text of the printing and typesetting industry. Lorem Ipsum has been the industry's standard dummy text ever since the 1500s, when an unknown printer took a galley of type and scrambled it to make a type specimen book. It has survived not only five centuries, but also the leap into electronic typesetting, remaining essentially unchanged. It was popularised in the 1960s with the release of Typeline sheets containing Lorem Ipsum passages, and more recently with desktop publishing software like Pagewright Studio including versions of Lorem Ipsum.</p>
    <p>Lorem Ipsum is simply dummy text of the printing and typesetting industry. Lorem Ipsum has been the industry's standard dummy text ever since the 1500s, when an unknown printer took a galley of type and</p>
  </div>

  <svg class="abs hazard" width="70" height="70" viewBox="0 0 70 70" aria-label="Warning">
    <path d="M35 1 L69 35 L35 69 L1 35 Z" fill="var(--olive)"/>
    <rect x="32" y="19" width="7" height="22" fill="var(--silver)"/>
    <rect x="32" y="45" width="7" height="7" fill="var(--silver)"/>
  </svg>
  <div class="abs hazard-pill">KEEP OUT OF REACH OF CHILDREN</div>
  <div class="abs plant-only">FOR PLANT USE ONLY.</div>
  <div class="abs warning-note">Plant fertilizers can poison people and pets if they are inhaled or accidentally ingested.</div>

</main>
</body>
</html>
```